2014 Wall Calendar Needed

I need a 2014 wall calendar design tweaked for my business Tolvane Building Advisors. We are a construction scheduling company you can check out our website www.advisetolvane.example . I had calendars designed last year (attachment #1) that I was pretty happy with but need the following improvements:

1. The Colors on the calendar and the logo must match - Notice the blue on the calendar and the blue on the header are different.

2. The calendar must contain at least 2, preferably 3 months from the end of 2013, and the beginning of 2015. (Some suggested layouts in Attachment #2 and #3)

3. The calendar must have out new "cloud" logo (Attachment #4) and website URL: cloud.advisetolvane.example

4. The calendar should contain the original logo (attachment #5) , and verbiage somewhere:
TOLVANE Building Advisors; Project Solutions; Scheduling, Earned Value Management, Dispute Resolution, 4D Scheduling, Application Cloud Solutions;

5. The contact information:
4372 Merrow Lane Suite 500
Silver Spring, MD 20910
Phone 301 555 7162
www.advisetolvane.example

6. The calendar should highlight week numbers and all major American and religious holidays (the holidays on the current calendar are more than enough, as are the week numbers)
Updates

The attachments have been uploaded. Additionally, you cal follow this link to download the attachments referenced in the posting.

 LINK-> https://advisetolvane.filedrop.example/d/k7pq2291058830417 
 

Target Market(s)

This poster will be sitting in a construction manager's office on the wall and will be used for "at a glance" planning

Industry/Entity Type

Construction

Requirements
Must have
• 1. Contact Information
2. Tolvane Logo (attachment #5
3. Tolvane Cloud Logo (Attachment #4)
4. 2014 Calendar year
5. at least 2, preferrably 3 months from the surrounding years (Oct Nov Dec 2013 and Jan Feb March of 2015)
6. Major American and Religious holidays
7. Must be able to print on standard poster size: 24X36 INCHES etc.
Nice to have
• Under each month in small font, I would like to have "anticipated weather days *" followed by a number. This number will indicate the anticipated days of inclement weather. I WILL RESEARCH SUPPLY THESE NUMBERS AFTER I CHOOSE THE FINAL DESIGN, these numbers will range from 1-10. At the bottom of the calendar will be an asterisk (*) which references the above statement and reads: "these estimates based on 5 day workweek in the Washington DC/VA area - may vary from contract to contract" this should also be in small font.

```html
<!DOCTYPE html>
<html lang="en">
<head>
<meta charset="utf-8">
<title>Tolvane Building Advisors – 2014 Project Calendar</title>
<link rel="stylesheet" href="https://fonts.googleapis.com/css2?family=PT+Sans:wght@400;700&family=PT+Sans+Narrow:wght@700&display=swap">
<style>
:root{
  --navy:#24235f;
  --gold:#e2a41d;
  --grey:#8e8e8e;
  --cream:#f5f0de;
  --ink:#1b1b1b;
  --page:#ffffff;
}
*{box-sizing:border-box;margin:0;padding:0}
html,body{width:1200px;height:1000px;overflow:hidden;background:var(--page)}
body{font-family:"PT Sans",Arial,sans-serif;position:relative}
.poster{position:absolute;left:285px;top:18px;width:630px;height:964px;background:var(--cream);overflow:hidden;box-shadow:0 2px 10px rgba(0,0,0,.25)}
.backdrop{position:absolute;left:0;top:62px;width:100%;height:740px;background:linear-gradient(90deg,rgba(214,205,160,0),rgba(200,195,140,.35) 50%,rgba(214,205,160,0))}
.header{position:absolute;left:0;top:0;width:100%;height:62px;background:var(--navy);color:#fff}
.year{position:absolute;left:14px;top:12px;font:700 36px/1 "PT Sans Narrow",sans-serif;color:var(--gold)}
.title{position:absolute;left:100px;top:20px;font:700 19px/1 "PT Sans Narrow",sans-serif}
.services{position:absolute;left:230px;top:10px;font-size:10px;line-height:15px;width:290px;text-align:center}
.services .dot{display:inline-block;width:6px;height:6px;border-radius:50%;background:var(--gold);margin:0 6px 1px}
.cloud-brand{position:absolute;right:12px;top:9px;text-align:right}
.cloud-brand .name{font:700 15px/1 "PT Sans",sans-serif;color:#fff}
.cloud-brand .name::before{content:"";display:inline-block;width:10px;height:10px;background:var(--gold);margin-right:5px}
.cloud-brand .url{font-size:8px;margin-top:4px;color:#dcdcf0}
.months{position:absolute;left:12px;top:68px;width:608px;height:732px;display:grid;grid-template-columns:repeat(3,1fr);grid-template-rows:repeat(6,122px);grid-auto-flow:column;column-gap:14px}
.month{border-bottom:1px solid var(--navy);padding-top:2px;position:relative}
.month h2{font:700 15px/17px "PT Sans Narrow",sans-serif;color:var(--navy);padding-left:22px}
.month.adjacent h2{color:var(--grey)}
.weekdays,.days{display:grid;grid-template-columns:22px repeat(7,1fr);text-align:center}
.weekdays span{font:700 9px/12px "PT Sans",sans-serif;color:var(--ink)}
.weekdays span:nth-child(8n+2),.weekdays span:nth-child(8n){color:var(--gold)}
.weekdays span:nth-child(8n+7){color:var(--navy)}
.days b,.days i{font:700 12px/14px "PT Sans",sans-serif;color:var(--ink);font-style:normal}
.days b:nth-child(8n+2),.days b:nth-child(8n){color:var(--gold)}
.days b:nth-child(8n+7){color:var(--navy)}
.days b.hol{color:var(--gold);text-decoration:underline;text-underline-offset:2px}
.days .wk{font:400 6px/14px "PT Sans",sans-serif;color:var(--ink);text-align:left;white-space:nowrap}
.weather{position:absolute;left:22px;bottom:1px;font-size:5px;line-height:7px;letter-spacing:.3px;text-transform:uppercase;color:var(--ink)}
.footer{position:absolute;left:0;bottom:0;width:100%;height:162px}
.footer svg{position:absolute;left:0;top:0}
.brand{position:absolute;left:28px;top:66px;font:700 19px/1 "PT Sans",sans-serif;color:var(--navy)}
.brand::before{content:"";display:inline-block;width:15px;height:15px;background:var(--navy);margin-right:7px;vertical-align:-1px}
.address{position:absolute;right:26px;top:86px;font-size:11px;line-height:15px;color:#fff;text-align:right}
.phone{position:absolute;left:30px;bottom:12px;font-size:14px;line-height:18px;color:#fff}
.web{position:absolute;left:240px;bottom:12px;font-size:15px;line-height:18px;color:#fff}
</style>
</head>
<body>
<div class="poster">
  <div class="backdrop" role="img" aria-label="Faint bamboo stalks and leaves behind the calendar grid"></div>

  <header class="header">
    <div class="year">2014</div>
    <div class="title">Project Solutions</div>
    <div class="services">Scheduling<span class="dot"></span>Earned Value Management<span class="dot"></span>Dispute Resolution<br>4D Scheduling<span class="dot"></span>Application Cloud Solutions</div>
    <div class="cloud-brand"><div class="name">Tolvane</div><div class="url">cloud.advisetolvane.example</div></div>
  </header>

  <main class="months">
    <section class="month adjacent"><h2>October</h2>
      <div class="weekdays"><span></span><span>Sun</span><span>Mon</span><span>Tue</span><span>Wed</span><span>Thu</span><span>Fri</span><span>Sat</span></div>
      <div class="days">
        <i class="wk">Wk 40</i><i></i><i></i><b>1</b><b>2</b><b>3</b><b>4</b><b>5</b>
        <i class="wk">Wk 41</i><b>6</b><b>7</b><b>8</b><b>9</b><b>10</b><b>11</b><b>12</b>
        <i class="wk">Wk 42</i><b>13</b><b class="hol">14</b><b>15</b><b>16</b><b>17</b><b>18</b><b>19</b>
        <i class="wk">Wk 43</i><b>20</b><b>21</b><b>22</b><b>23</b><b>24</b><b>25</b><b>26</b>
        <i class="wk">Wk 44</i><b>27</b><b>28</b><b>29</b><b>30</b><b>31</b></div>
      <p class="weather">Anticipated weather days:</p></section>
    <section class="month adjacent"><h2>November</h2>
      <div class="weekdays"><span></span><span>Sun</span><span>Mon</span><span>Tue</span><span>Wed</span><span>Thu</span><span>Fri</span><span>Sat</span></div>
      <div class="days">
        <i class="wk">Wk 44</i><i></i><i></i><i></i><i></i><i></i><b>1</b><b>2</b>
        <i class="wk">Wk 45</i><b>3</b><b>4</b><b>5</b><b>6</b><b>7</b><b>8</b><b>9</b>
        <i class="wk">Wk 46</i><b>10</b><b class="hol">11</b><b>12</b><b>13</b><b>14</b><b>15</b><b>16</b>
        <i class="wk">Wk 47</i><b>17</b><b>18</b><b>19</b><b>20</b><b>21</b><b>22</b><b>23</b>
        <i class="wk">Wk 48</i><b>24</b><b>25</b><b>26</b><b>27</b><b class="hol">28</b><b>29</b><b>30</b></div>
      <p class="weather">Anticipated weather days:</p></section>
    <section class="month adjacent"><h2>December</h2>
      <div class="weekdays"><span></span><span>Sun</span><span>Mon</span><span>Tue</span><span>Wed</span><span>Thu</span><span>Fri</span><span>Sat</span></div>
      <div class="days">
        <i class="wk">Wk 49</i><b>1</b><b>2</b><b>3</b><b>4</b><b>5</b><b>6</b><b>7</b>
        <i class="wk">Wk 50</i><b>8</b><b>9</b><b>10</b><b>11</b><b>12</b><b>13</b><b>14</b>
        <i class="wk">Wk 51</i><b>15</b><b>16</b><b>17</b><b>18</b><b>19</b><b>20</b><b>21</b>
        <i class="wk">Wk 52</i><b>22</b><b>23</b><b>24</b><b class="hol">25</b><b>26</b><b>27</b><b>28</b>
        <i class="wk">Wk 1</i><b>29</b><b>30</b><b>31</b></div>
      <p class="weather">Anticipated weather days:</p></section>
    <section class="month"><h2>January</h2>
      <div class="weekdays"><span></span><span>Sun</span><span>Mon</span><span>Tue</span><span>Wed</span><span>Thu</span><span>Fri</span><span>Sat</span></div>
      <div class="days">
        <i class="wk">Wk 1</i><i></i><i></i><i></i><b class="hol">1</b><b>2</b><b>3</b><b>4</b>
        <i class="wk">Wk 2</i><b>5</b><b>6</b><b>7</b><b>8</b><b>9</b><b>10</b><b>11</b>
        <i class="wk">Wk 3</i><b>12</b><b>13</b><b>14</b><b>15</b><b>16</b><b>17</b><b>18</b>
        <i class="wk">Wk 4</i><b>19</b><b class="hol">20</b><b>21</b><b>22</b><b>23</b><b>24</b><b>25</b>
        <i class="wk">Wk 5</i><b>26</b><b>27</b><b>28</b><b>29</b><b>30</b><b>31</b></div>
      <p class="weather">Anticipated weather days:</p></section>
    <section class="month"><h2>February</h2>
      <div class="weekdays"><span></span><span>Sun</span><span>Mon</span><span>Tue</span><span>Wed</span><span>Thu</span><span>Fri</span><span>Sat</span></div>
      <div class="days">
        <i class="wk">Wk 5</i><i></i><i></i><i></i><i></i><i></i><i></i><b>1</b>
        <i class="wk">Wk 6</i><b>2</b><b>3</b><b>4</b><b>5</b><b>6</b><b>7</b><b>8</b>
        <i class="wk">Wk 7</i><b>9</b><b>10</b><b>11</b><b>12</b><b>13</b><b class="hol">14</b><b>15</b>
        <i class="wk">Wk 8</i><b>16</b><b class="hol">17</b><b>18</b><b>19</b><b>20</b><b>21</b><b>22</b>
        <i class="wk">Wk 9</i><b>23</b><b>24</b><b>25</b><b>26</b><b>27</b><b>28</b></div>
      <p class="weather">Anticipated weather days:</p></section>
    <section class="month"><h2>March</h2>
      <div class="weekdays"><span></span><span>Sun</span><span>Mon</span><span>Tue</span><span>Wed</span><span>Thu</span><span>Fri</span><span>Sat</span></div>
      <div class="days">
        <i class="wk">Wk 9</i><i></i><i></i><i></i><i></i><i></i><i></i><b>1</b>
        <i class="wk">Wk 10</i><b>2</b><b>3</b><b>4</b><b>5</b><b>6</b><b>7</b><b>8</b>
        <i class="wk">Wk 11</i><b>9</b><b>10</b><b>11</b><b>12</b><b>13</b><b>14</b><b>15</b>
        <i class="wk">Wk 12</i><b>16</b><b class="hol">17</b><b>18</b><b>19</b><b>20</b><b>21</b><b>22</b>
        <i class="wk">Wk 13</i><b>23</b><b>24</b><b>25</b><b>26</b><b>27</b><b>28</b><b>29</b>
        <i class="wk">Wk 14</i><b>30</b><b>31</b></div>
      <p class="weather">Anticipated weather days:</p></section>

    <section class="month"><h2>April</h2>
      <div class="weekdays"><span></span><span>Sun</span><span>Mon</span><span>Tue</span><span>Wed</span><span>Thu</span><span>Fri</span><span>Sat</span></div>
      <div class="days">
        <i class="wk">Wk 14</i><i></i><i></i><b>1</b><b>2</b><b>3</b><b>4</b><b>5</b>
        <i class="wk">Wk 15</i><b>6</b><b>7</b><b>8</b><b>9</b><b>10</b><b>11</b><b>12</b>
        <i class="wk">Wk 16</i><b>13</b><b>14</b><b>15</b><b>16</b><b>17</b><b class="hol">18</b><b>19</b>
        <i class="wk">Wk 17</i><b class="hol">20</b><b>21</b><b>22</b><b>23</b><b>24</b><b>25</b><b>26</b>
        <i class="wk">Wk 18</i><b>27</b><b>28</b><b>29</b><b>30</b></div>
      <p class="weather">Anticipated weather days:</p></section>
    <section class="month"><h2>May</h2>
      <div class="weekdays"><span></span><span>Sun</span><span>Mon</span><span>Tue</span><span>Wed</span><span>Thu</span><span>Fri</span><span>Sat</span></div>
      <div class="days">
        <i class="wk">Wk 18</i><i></i><i></i><i></i><i></i><b>1</b><b>2</b><b>3</b>
        <i class="wk">Wk 19</i><b>4</b><b>5</b><b>6</b><b>7</b><b>8</b><b>9</b><b>10</b>
        <i class="wk">Wk 20</i><b class="hol">11</b><b>12</b><b>13</b><b>14</b><b>15</b><b>16</b><b>17</b>
        <i class="wk">Wk 21</i><b>18</b><b>19</b><b>20</b><b>21</b><b>22</b><b>23</b><b>24</b>
        <i class="wk">Wk 22</i><b>25</b><b class="hol">26</b><b>27</b><b>28</b><b>29</b><b>30</b><b>31</b></div>
      <p class="weather">Anticipated weather days:</p></section>
    <section class="month"><h2>June</h2>
      <div class="weekdays"><span></span><span>Sun</span><span>Mon</span><span>Tue</span><span>Wed</span><span>Thu</span><span>Fri</span><span>Sat</span></div>
      <div class="days">
        <i class="wk">Wk 23</i><b>1</b><b>2</b><b>3</b><b>4</b><b>5</b><b>6</b><b>7</b>
        <i class="wk">Wk 24</i><b>8</b><b>9</b><b>10</b><b>11</b><b>12</b><b>13</b><b>14</b>
        <i class="wk">Wk 25</i><b class="hol">15</b><b>16</b><b>17</b><b>18</b><b>19</b><b>20</b><b>21</b>
        <i class="wk">Wk 26</i><b>22</b><b>23</b><b>24</b><b>25</b><b>26</b><b>27</b><b>28</b>
        <i class="wk">Wk 27</i><b>29</b><b>30</b></div>
      <p class="weather">Anticipated weather days:</p></section>
    <section class="month"><h2>July</h2>
      <div class="weekdays"><span></span><span>Sun</span><span>Mon</span><span>Tue</span><span>Wed</span><span>Thu</span><span>Fri</span><span>Sat</span></div>
      <div class="days">
        <i class="wk">Wk 27</i><i></i><i></i><b>1</b><b>2</b><b>3</b><b class="hol">4</b><b>5</b>
        <i class="wk">Wk 28</i><b>6</b><b>7</b><b>8</b><b>9</b><b>10</b><b>11</b><b>12</b>
        <i class="wk">Wk 29</i><b>13</b><b>14</b><b>15</b><b>16</b><b>17</b><b>18</b><b>19</b>
        <i class="wk">Wk 30</i><b>20</b><b>21</b><b>22</b><b>23</b><b>24</b><b>25</b><b>26</b>
        <i class="wk">Wk 31</i><b>27</b><b>28</b><b>29</b><b>30</b><b>31</b></div>
      <p class="weather">Anticipated weather days:</p></section>
    <section class="month"><h2>August</h2>
      <div class="weekdays"><span></span><span>Sun</span><span>Mon</span><span>Tue</span><span>Wed</span><span>Thu</span><span>Fri</span><span>Sat</span></div>
      <div class="days">
        <i class="wk">Wk 31</i><i></i><i></i><i></i><i></i><i></i><b>1</b><b>2</b>
        <i class="wk">Wk 32</i><b>3</b><b>4</b><b>5</b><b>6</b><b>7</b><b>8</b><b>9</b>
        <i class="wk">Wk 33</i><b>10</b><b>11</b><b>12</b><b>13</b><b>14</b><b>15</b><b>16</b>
        <i class="wk">Wk 34</i><b>17</b><b>18</b><b>19</b><b>20</b><b>21</b><b>22</b><b>23</b>
        <i class="wk">Wk 35</i><b>24</b><b>25</b><b>26</b><b>27</b><b>28</b><b>29</b><b>30</b>
        <i class="wk">Wk 36</i><b>31</b></div>
      <p class="weather">Anticipated weather days:</p></section>
    <section class="month"><h2>September</h2>
      <div class="weekdays"><span></span><span>Sun</span><span>Mon</span><span>Tue</span><span>Wed</span><span>Thu</span><span>Fri</span><span>Sat</span></div>
      <div class="days">
        <i class="wk">Wk 36</i><i></i><b class="hol">1</b><b>2</b><b>3</b><b>4</b><b>5</b><b>6</b>
        <i class="wk">Wk 37</i><b>7</b><b>8</b><b>9</b><b>10</b><b>11</b><b>12</b><b>13</b>
        <i class="wk">Wk 38</i><b>14</b><b>15</b><b>16</b><b>17</b><b>18</b><b>19</b><b>20</b>
        <i class="wk">Wk 39</i><b>21</b><b>22</b><b>23</b><b>24</b><b>25</b><b>26</b><b>27</b>
        <i class="wk">Wk 40</i><b>28</b><b>29</b><b>30</b></div>
      <p class="weather">Anticipated weather days:</p></section>

    <section class="month"><h2>October</h2>
      <div class="weekdays"><span></span><span>Sun</span><span>Mon</span><span>Tue</span><span>Wed</span><span>Thu</span><span>Fri</span><span>Sat</span></div>
      <div class="days">
        <i class="wk">Wk 40</i><i></i><i></i><i></i><b>1</b><b>2</b><b>3</b><b>4</b>
        <i class="wk">Wk 41</i><b>5</b><b>6</b><b>7</b><b>8</b><b>9</b><b>10</b><b>11</b>
        <i class="wk">Wk 42</i><b>12</b><b class="hol">13</b><b>14</b><b>15</b><b>16</b><b>17</b><b>18</b>
        <i class="wk">Wk 43</i><b>19</b><b>20</b><b>21</b><b>22</b><b>23</b><b>24</b><b>25</b>
        <i class="wk">Wk 44</i><b>26</b><b>27</b><b>28</b><b>29</b><b>30</b><b>31</b></div>
      <p class="weather">Anticipated weather days:</p></section>
    <section class="month"><h2>November</h2>
      <div class="weekdays"><span></span><span>Sun</span><span>Mon</span><span>Tue</span><span>Wed</span><span>Thu</span><span>Fri</span><span>Sat</span></div>
      <div class="days">
        <i class="wk">Wk 44</i><i></i><i></i><i></i><i></i><i></i><i></i><b>1</b>
        <i class="wk">Wk 45</i><b>2</b><b>3</b><b>4</b><b>5</b><b>6</b><b>7</b><b>8</b>
        <i class="wk">Wk 46</i><b>9</b><b>10</b><b class="hol">11</b><b>12</b><b>13</b><b>14</b><b>15</b>
        <i class="wk">Wk 47</i><b>16</b><b>17</b><b>18</b><b>19</b><b>20</b><b>21</b><b>22</b>
        <i class="wk">Wk 48</i><b>23</b><b>24</b><b>25</b><b>26</b><b class="hol">27</b><b>28</b><b>29</b>
        <i class="wk">Wk 49</i><b>30</b></div>
      <p class="weather">Anticipated weather days:</p></section>
    <section class="month"><h2>December</h2>
      <div class="weekdays"><span></span><span>Sun</span><span>Mon</span><span>Tue</span><span>Wed</span><span>Thu</span><span>Fri</span><span>Sat</span></div>
      <div class="days">
        <i class="wk">Wk 49</i><i></i><b>1</b><b>2</b><b>3</b><b>4</b><b>5</b><b>6</b>
        <i class="wk">Wk 50</i><b>7</b><b>8</b><b>9</b><b>10</b><b>11</b><b>12</b><b>13</b>
        <i class="wk">Wk 51</i><b>14</b><b>15</b><b>16</b><b class="hol">17</b><b>18</b><b>19</b><b>20</b>
        <i class="wk">Wk 52</i><b>21</b><b>22</b><b>23</b><b>24</b><b class="hol">25</b><b>26</b><b>27</b>
        <i class="wk">Wk 1</i><b>28</b><b>29</b><b>30</b><b>31</b></div>
      <p class="weather">Anticipated weather days:</p></section>
    <section class="month adjacent"><h2>January</h2>
      <div class="weekdays"><span></span><span>Sun</span><span>Mon</span><span>Tue</span><span>Wed</span><span>Thu</span><span>Fri</span><span>Sat</span></div>
      <div class="days">
        <i class="wk">Wk 1</i><i></i><i></i><i></i><i></i><b class="hol">1</b><b>2</b><b>3</b>
        <i class="wk">Wk 2</i><b>4</b><b>5</b><b>6</b><b>7</b><b>8</b><b>9</b><b>10</b>
        <i class="wk">Wk 3</i><b>11</b><b>12</b><b>13</b><b>14</b><b>15</b><b>16</b><b>17</b>
        <i class="wk">Wk 4</i><b>18</b><b class="hol">19</b><b>20</b><b>21</b><b>22</b><b>23</b><b>24</b>
        <i class="wk">Wk 5</i><b>25</b><b>26</b><b>27</b><b>28</b><b>29</b><b>30</b><b>31</b></div>
      <p class="weather">Anticipated weather days:</p></section>
    <section class="month adjacent"><h2>February</h2>
      <div class="weekdays"><span></span><span>Sun</span><span>Mon</span><span>Tue</span><span>Wed</span><span>Thu</span><span>Fri</span><span>Sat</span></div>
      <div class="days">
        <i class="wk">Wk 6</i><b>1</b><b>2</b><b>3</b><b>4</b><b>5</b><b>6</b><b>7</b>
        <i class="wk">Wk 7</i><b>8</b><b>9</b><b>10</b><b>11</b><b>12</b><b>13</b><b>14</b>
        <i class="wk">Wk 8</i><b>15</b><b class="hol">16</b><b>17</b><b>18</b><b>19</b><b>20</b><b>21</b>
        <i class="wk">Wk 9</i><b>22</b><b>23</b><b>24</b><b>25</b><b>26</b><b>27</b><b>28</b></div>
      <p class="weather">Anticipated weather days:</p></section>
    <section class="month adjacent"><h2>March</h2>
      <div class="weekdays"><span></span><span>Sun</span><span>Mon</span><span>Tue</span><span>Wed</span><span>Thu</span><span>Fri</span><span>Sat</span></div>
      <div class="days">
        <i class="wk">Wk 10</i><b>1</b><b>2</b><b>3</b><b>4</b><b>5</b><b>6</b><b>7</b>
        <i class="wk">Wk 11</i><b>8</b><b>9</b><b>10</b><b>11</b><b>12</b><b>13</b><b>14</b>
        <i class="wk">Wk 12</i><b>15</b><b>16</b><b class="hol">17</b><b>18</b><b>19</b><b>20</b><b>21</b>
        <i class="wk">Wk 13</i><b>22</b><b>23</b><b>24</b><b>25</b><b>26</b><b>27</b><b>28</b>
        <i class="wk">Wk 14</i><b>29</b><b>30</b><b>31</b></div>
      <p class="weather">Anticipated weather days:</p></section>
  </main>

  <footer class="footer">
    <svg width="630" height="162" viewBox="0 0 630 162" aria-hidden="true">
      <path d="M0 124 Q360 116 630 22 L630 162 L0 162 Z" fill="var(--navy)"/>
      <path d="M0 120 Q360 112 630 18" fill="none" stroke="var(--gold)" stroke-width="5"/>
    </svg>
    <div class="brand">TOLVANE Building Advisors</div>
    <div class="address">4372 Merrow Lane Suite 500<br>Silver Spring, MD 20910</div>
    <div class="phone">Phone 301 555 7162</div>
    <div class="web">www.advisetolvane.example</div>
  </footer>
</div>
</body>
</html>
```